Web Design Project: Executive Coach

PLEASE check out http://tarvell.com.sg/x/PixelGuild/PixelGuild_Brief/Blank.html

It is a better description of what I am after. It includes everything in this brief and in an easier format. (And...I don't have your design skills, so it doesn't look great.)

========

What the site offers
-
I am about to launch a one-person company that provides three services:
1) executive coaching
2) leadership training
3) psychotherapy to adults

My Unique Selling Point
-
My unique selling point is that I am a coach who is also a relatively senior psychologist. However, psychologists can be seen as scary and that may put people off.

The Biggest Challenge: The Target Audience
-
One challenge is that because I sell 3 services, I want to appeal to more than one demographic. They are:

1) The representative from HR of a company who wants to buy a leadership course or find a coach for an executive in the company. (Usually mid-40’s and older.)

2) The executives who will take the selection made by the head of HR and may choose me from 3 or 4 other options. (Usually late 30’s to mid 40’s. Both men and women. From multinational companies.)

3) Psychotherapy clients who are coming to be directly, not via HR, and who don’t want to feel insecure that they aren’t executives but still may be a good fit to work with me. (More women than men. Age 34-45. Typically have some European or American exposure.)

The Problem
-
The executives I see may or may not have some psychological concerns, but most will quite like that I am a psychologist as long as I’m not “scary” but “kind”. (Kind is key.) So while it is important to show I am a therapist, I don't want it to make executives embarrassed when a colleague says “Oh, I looked at this guy’s website. You aren't in therapy are you?”

As mentioned above, please check out the following link: http://tarvell.com.sg/x/PixelGuild/PixelGuild_Brief/Blank.html

________
Please note, I originally posted this as 584207 Executive Coaching, Leadership Training, and Psychotherapy Website. With the help of one designer and also PixelGuild customer support, I realized that I had requested only the design of a website, not the coding. I had offered the maximum amount, US$1000 (refundable). I am resubmitting the project here and I have guaranteed the funds. I am lowering the payment as I am now aware that I was only asking for design. I apologize for any inconvenience. And thank your for being interested in this project.
Updates

Reason: I would love to get started on the coding next week. So I hope to get your proposals in the next 3 days.

Target Market(s)

Primary audience: 34-44 year old men and women with some European / North American exposure

Industry/Entity Type

Leadership

Requirements
Must have
• Video on home page
Nice to have
• I would like have quotes slide in to a couple of the pages. These may have a photo of the author attached.

I would like WorkLoop integration with my business's WorkLoop page. (I haven't made one yet, so I'm not sure how it works.)

```html
<!DOCTYPE html>
<html lang="en">
<head>
<meta charset="utf-8">
<title>Tarvell Consulting</title>
<link href="https://fonts.googleapis.com/css2?family=Open+Sans:wght@400;600&family=Source+Sans+3:wght@400;600;700&display=swap" rel="stylesheet">
<style>
:root{
  --teal:#1d5654;
  --teal-dark:#163f3e;
  --link:#2a7675;
  --page:#ececec;
  --panel:#ffffff;
  --line:#dcdcdc;
  --text:#555555;
  --heading:#222222;
  --footer:#2b2b2b;
  --footer-text:#6e6e6e;
  --footer-head:#7d7d7d;
  --widget-blue:#1b6aa0;
}
*{box-sizing:border-box;margin:0;padding:0}
html,body{width:757px;height:1200px;overflow:hidden}
body{position:relative;background:var(--page);font-family:"Open Sans",Arial,sans-serif;color:var(--text)}

/* header */
.topbar{position:absolute;left:0;top:0;width:757px;height:50px;background:linear-gradient(#f7f7f7,#e2e2e2);border-top:6px solid var(--teal);box-shadow:0 2px 4px rgba(0,0,0,.18)}
.nav{position:absolute;top:18px;left:94px;display:flex;font-family:"Source Sans 3",sans-serif;font-size:10px;color:#555;letter-spacing:.3px}
.nav a{display:block;padding:3px 8px;color:#555;text-decoration:none;margin-right:7px}
.nav a.active{background:linear-gradient(#e4e4e4,#d2d2d2);border:1px solid #c4c4c4;border-radius:2px}
.social{position:absolute;top:25px;left:481px;display:flex;gap:3px}
.social span{width:10px;height:10px;border-radius:2px}
.search{position:absolute;left:556px;top:22px;width:100px;height:17px;border:1px solid #c9c9c9;border-radius:9px;background:#fff;font-size:9px;color:#333;padding:2px 8px}
.search svg{position:absolute;right:6px;top:3px}

.masthead{position:absolute;left:97px;top:64px;display:flex;align-items:baseline;gap:7px;white-space:nowrap}
.brand{font-family:"Source Sans 3",sans-serif;font-size:31px;color:var(--teal);letter-spacing:-.5px}
.tagline{font-size:8px;color:#777}

/* hero */
.panel{position:absolute;background:var(--panel);border:1px solid #e0e0e0;box-shadow:0 1px 2px rgba(0,0,0,.05)}
.hero{left:82px;top:120px;width:592px;height:214px}
.hero h1{position:absolute;left:19px;top:20px;font-weight:400;font-size:20px;line-height:23px;color:var(--heading)}
.hero p{position:absolute;left:19px;top:69px;width:262px;font-size:9.2px;line-height:15px;color:#555}
.btn{position:absolute;left:19px;top:164px;width:73px;height:26px;border:1px solid #c8c8c8;border-radius:3px;background:linear-gradient(#f9f9f9,#e1e1e1);font-size:10px;color:#444;text-align:center;line-height:24px}
.video{position:absolute;left:291px;top:23px;width:267px;height:170px;border:4px solid #e4e4e4;border-radius:6px;box-shadow:0 0 3px rgba(0,0,0,.25)}
.video .media{width:100%;height:100%;background:linear-gradient(100deg,#e9ecee 0%,#d6dadd 55%,#b58b62 75%,#8f6440 100%)}
.video svg{position:absolute;left:112px;top:63px}

/* testimonials */
.quotes{left:82px;top:348px;width:592px;height:77px}
.quote{position:absolute;top:18px;width:190px}
.avatar{position:absolute;left:0;top:0;width:31px;height:31px;border:1px solid #ccc;background:linear-gradient(#2c2c2c,#6b6b6b)}
.quote p{position:absolute;left:38px;top:-2px;width:150px;font-size:7px;line-height:10.5px;color:#444}
.quote .who{position:absolute;left:38px;top:33px;font-size:7px;color:#444;white-space:nowrap}
.quote .who b{color:var(--teal);font-weight:600}
.qdiv{position:absolute;top:10px;width:1px;height:57px;background:#e2e2e2}
.arrow{position:absolute;top:380px}

/* services */
.card{top:440px;width:188px;height:254px}
.card h2{position:absolute;left:16px;top:11px;font-family:"Source Sans 3",sans-serif;font-weight:600;font-size:16.5px;color:var(--heading);white-space:nowrap}
.card .rule{position:absolute;left:16px;top:33px;width:156px;height:2px;background:#dedede}
.card .photo{position:absolute;left:18px;top:47px;width:151px;height:66px}
.card p{position:absolute;left:18px;top:124px;width:158px;font-family:"Source Sans 3",sans-serif;font-size:8.6px;line-height:15.4px;color:#555}

/* clients */
.clients-title{position:absolute;left:98px;top:725px;font-family:"Source Sans 3",sans-serif;font-weight:700;font-size:17px;color:var(--heading)}
.clients-rule{position:absolute;left:98px;top:748px;width:559px;height:2px;background:#d8d8d8}
.client{position:absolute;width:260px;height:100px}
.client .thumb{position:absolute;left:0;top:0;width:30px;height:30px;background:#dcdcdc}
.client h3{position:absolute;left:44px;top:-2px;font-family:"Source Sans 3",sans-serif;font-weight:700;font-size:13px;color:var(--teal)}
.client p{position:absolute;left:44px;top:18px;width:205px;font-size:8.2px;line-height:16px;color:#555}
.client .more{position:absolute;left:44px;top:68px;width:52px;height:13px;border:1px solid #c8c8c8;border-radius:7px;background:linear-gradient(#fff,#e8e8e8);font-size:6.8px;font-weight:600;color:#333;text-align:center;line-height:11px}

/* footer */
.footer{position:absolute;left:0;top:984px;width:757px;height:216px;background:var(--footer);border-top:7px solid var(--teal-dark)}
.footer h4{position:absolute;top:28px;font-family:"Source Sans 3",sans-serif;font-weight:600;font-size:19px;color:var(--footer-head)}
.fdiv{position:absolute;top:18px;width:1px;height:156px;background:#3c3c3c}
.about-text{position:absolute;left:89px;top:60px;width:160px;font-size:8px;line-height:14.2px;color:var(--footer-text)}
.posts{position:absolute;left:279px;top:62px;width:110px;font-size:9px;line-height:11.5px;list-style:none}
.posts li{margin-bottom:12px;color:var(--link)}
.posts a{color:var(--link);text-decoration:underline}
.widget{position:absolute;left:439px;top:34px;width:230px;height:130px;background:#fff;border:4px solid #e5e5e5;border-radius:4px}
.widget .name{position:absolute;left:8px;top:10px;width:140px;font-weight:600;font-size:12.5px;line-height:15px;color:var(--widget-blue)}
.widget .logo{position:absolute;left:163px;top:17px;width:52px;height:47px;background:var(--teal-dark);color:#fff;font-size:8px;text-align:center;line-height:47px}
.widget .desc{position:absolute;left:8px;top:46px;width:146px;font-family:Arial,sans-serif;font-size:8px;line-height:10px;color:#333}
.widget .meta{position:absolute;left:8px;top:90px;font-family:Arial,sans-serif;font-size:7.5px;color:#666}
.widget .follow{position:absolute;left:8px;top:104px;width:60px;height:14px;border:1px solid #9fb9d1;border-radius:2px;background:linear-gradient(#f3f8fc,#dce8f2);font-family:Arial,sans-serif;font-size:7.5px;color:#345;line-height:12px;padding-left:18px}
.widget .follow i{position:absolute;left:4px;top:2px;width:8px;height:8px;background:var(--widget-blue);border-radius:1px}
.frule{position:absolute;left:77px;top:178px;width:600px;height:1px;background:#3a3a3a}
.copy{position:absolute;left:0;top:196px;width:757px;text-align:center;font-size:6.8px;color:#8a8a8a}
</style>
</head>
<body>

<header class="topbar">
  <nav class="nav">
    <a>HOME</a><a class="active">ABOUT</a><a>SERVICES</a><a>BLOG</a><a>CONTACT</a>
  </nav>
  <div class="social">
    <span style="background:#e8893a"></span><span style="background:#4fa9d8"></span><span style="background:#3b5d9c"></span><span style="background:#b5b5b5"></span><span style="background:#2f78a8"></span>
  </div>
  <div class="search">Search
    <svg width="10" height="10" viewBox="0 0 10 10"><circle cx="4" cy="4" r="3" fill="none" stroke="#999" stroke-width="1.4"/><line x1="6.2" y1="6.2" x2="9" y2="9" stroke="#999" stroke-width="1.6"/></svg>
  </div>
</header>

<div class="masthead">
  <div class="brand">Tarvell Consulting</div>
  <div class="tagline">Place short tag–line here.</div>
</div>

<section class="panel hero">
  <h1>Business Coaching for<br>Executives in Singapore</h1>
  <p>Lorem ipsum dolor sit amet, consectetur adipisicing elit, sed do eiusmod tempor incididunt ut labore et dolore magna aliqua. Ut enim ad minim veniam, quis nostrud exercitation ullamco laboris nisi ut aliquip ex ea commodo consequat. Duis aute irure dolor in reprehenderit in</p>
  <div class="btn">Learn More</div>
  <div class="video">
    <div class="media" role="img" aria-label="Video still: businessman with arms outstretched on top of a rocky cliff against a pale sky"></div>
    <svg width="34" height="34" viewBox="0 0 34 34"><circle cx="17" cy="17" r="16" fill="rgba(60,60,60,.75)"/><polygon points="13,10 25,17 13,24" fill="#fff"/></svg>
  </div>
</section>

<svg class="arrow" style="left:57px" width="14" height="18" viewBox="0 0 14 18"><polygon points="12,1 2,9 12,17" fill="#9a9a9a"/></svg>
<svg class="arrow" style="left:684px" width="14" height="18" viewBox="0 0 14 18"><polygon points="2,1 12,9 2,17" fill="#9a9a9a"/></svg>

<section class="panel quotes">
  <div class="quote" style="left:13px">
    <div class="avatar" role="img" aria-label="Portrait photo of the quote author"></div>
    <p>“Lorem ipsum dolor sit amet, consectetur adipisicing elit, sed do eiusmod tempor incididunt ut labore et dolore.”</p>
    <div class="who"><b>John Doe</b> &nbsp;CEO, Company Name</div>
  </div>
  <div class="qdiv" style="left:196px"></div>
  <div class="quote" style="left:210px">
    <div class="avatar" role="img" aria-label="Portrait photo of the quote author"></div>
    <p>“Lorem ipsum dolor sit amet, consectetur adipisicing elit, sed do eiusmod tempor incididunt ut labore et dolore.”</p>
    <div class="who"><b>John Doe</b> &nbsp;CEO, Company Name</div>
  </div>
  <div class="qdiv" style="left:394px"></div>
  <div class="quote" style="left:408px">
    <div class="avatar" role="img" aria-label="Portrait photo of the quote author"></div>
    <p>“Lorem ipsum dolor sit amet, consectetur adipisicing elit, sed do eiusmod tempor incididunt ut labore et dolore.”</p>
    <div class="who"><b>John Doe</b> &nbsp;CEO, Company Name</div>
  </div>
</section>

<section class="panel card" style="left:83px">
  <h2>Executive Coaching</h2><div class="rule"></div>
  <div class="photo" role="img" aria-label="Photo of a team of business people in suits" style="background:linear-gradient(90deg,#4a4a4a,#c9c9c9 40%,#e6d6bf 65%,#3d3d3d)"></div>
  <p>Lorem ipsum dolor sit amet, consectetur adipisicing elit, sed do eiusmod tempor incididunt ut labore et dolore magna aliqua. Ut enim ad minim veniam, quis nostrud exercitation ullamco laboris nisi ut aliquip ex ea commodo consequat. Duis aute irure dolor in reprehenderit in voluptate velit esse cillum dolore eu</p>
</section>
<section class="panel card" style="left:284px">
  <h2>Leadership Training</h2><div class="rule"></div>
  <div class="photo" role="img" aria-label="Photo of a hand selecting leadership keywords on a blue screen" style="background:linear-gradient(90deg,#3f5f86,#9db6d4 50%,#d4e0ee)"></div>
  <p>Lorem ipsum dolor sit amet, consectetur adipisicing elit, sed do eiusmod tempor incididunt ut labore et dolore magna aliqua. Ut enim ad minim veniam, quis nostrud exercitation ullamco laboris nisi ut aliquip ex ea commodo consequat. Duis aute irure dolor in reprehenderit in voluptate velit esse cillum dolore eu fugiat</p>
</section>
<section class="panel card" style="left:486px">
  <h2>Psychotherapy</h2><div class="rule"></div>
  <div class="photo" role="img" aria-label="Photo of a woman relaxing on a couch during a therapy session" style="background:linear-gradient(90deg,#b8a49a,#e8e3df 45%,#d9d4d0)"></div>
  <p>Lorem ipsum dolor sit amet, consectetur adipisicing elit, sed do eiusmod tempor incididunt ut labore et dolore magna aliqua. Ut enim ad minim veniam, quis nostrud exercitation ullamco laboris nisi ut aliquip ex ea commodo consequat. Duis aute irure dolor in reprehenderit in voluptate velit esse cillum dolore eu</p>
</section>

<h2 class="clients-title">Our Clients</h2>
<div class="clients-rule"></div>

<div class="client" style="left:101px;top:767px">
  <div class="thumb"></div><h3>Head of HR</h3>
  <p>Lorem ipsum dolor sit amet, consectetur adipisicing elit, sed do eiusmod tempor incididunt ut labore et dolore magna aliqua.</p>
  <div class="more">Read More</div>
</div>
<div class="client" style="left:378px;top:767px">
  <div class="thumb"></div><h3>Client Type #3</h3>
  <p>Lorem ipsum dolor sit amet, consectetur adipisicing elit, sed do eiusmod tempor incididunt ut labore et dolore magna aliqua.</p>
  <div class="more">Read More</div>
</div>
<div class="client" style="left:101px;top:871px">
  <div class="thumb"></div><h3>Executive Coach</h3>
  <p>Lorem ipsum dolor sit amet, consectetur adipisicing elit, sed do eiusmod tempor incididunt ut labore et dolore magna aliqua.</p>
  <div class="more">Read More</div>
</div>
<div class="client" style="left:378px;top:871px">
  <div class="thumb"></div><h3>Client Type #4</h3>
  <p>Lorem ipsum dolor sit amet, consectetur adipisicing elit, sed do eiusmod tempor incididunt ut labore et dolore magna aliqua.</p>
  <div class="more">Read More</div>
</div>

<footer class="footer">
  <h4 style="left:89px">About</h4>
  <p class="about-text">Lorem ipsum dolor sit amet, consectetur adipisicing elit, sed do eiusmod tempor incididunt ut labore et dolore magna aliqua. Ut enim ad minim veniam, quis nostrud exercitation ullamco laboris nisi ut aliquip ex ea commodo consequat.</p>
  <div class="fdiv" style="left:250px"></div>
  <h4 style="left:277px">Recent Posts</h4>
  <ul class="posts">
    <li>• <a>Mauris eget orci id leo</a><br>• <a>rhoncus volutpat</a></li>
    <li>• <a>Nullam auctor lorem</a></li>
    <li>• <a>Duis id eros sed dolor</a><br>• <a>fringilla lobortis</a></li>
  </ul>
  <div class="fdiv" style="left:414px"></div>
  <div class="widget">
    <div class="name">Tarvell Consulting Group</div>
    <div class="logo">Logo here</div>
    <div class="desc">Lorem ipsum dolor sit amet, consectetur adipisicing elit, sed do eiusmod tempor incididunt ut labore et dolore magna aliqua. Ut enim ad minim ...</div>
    <div class="meta">Address &nbsp;1-10 employees</div>
    <div class="follow"><i></i>Follow</div>
  </div>
  <div class="frule"></div>
  <div class="copy">Copyright Tarvell Consulting 2013 / &nbsp;All Rights Reserved.</div>
</footer>

</body>
</html>
```